training slide

We have an existing PPT template.

I am just looking for someone to make the attached slides better looking. If that goes well we have a whole bunch of presentations that need formatting in a similar style. Our customer base is made up of pharmaceutical and healthcare companies. we charge high end consultancy prices and it is very important our production value reflects this level of quality. We are not attached to the current PPT template and if anyone wants to re-visit that we would be very keen to see any ideas. We do however like our veraKorbell logo but you can lose the energy, experience etc.

Industry/Entity Type

Training

```html
<!DOCTYPE html>
<html lang="en">
<head>
<meta charset="utf-8">
<title>veraKorbell – slide set</title>
<link href="https://fonts.googleapis.com/css2?family=Open+Sans:wght@400;600;700&display=swap" rel="stylesheet">
<style>
  :root{
    --plum:#6b1a5a;
    --magenta:#e2358d;
    --magenta-line:#d6287f;
    --ink:#222;
    --grey-text:#444;
    --bullet:#b9b9b9;
    --diamond:#cfcfcf;
    --canvas:#ebe8e4;
    --energy:#a24a9e;
    --credibility:#38479b;
    --relationships:#f26522;
    --white:#fff;
  }
  *{box-sizing:border-box;margin:0;padding:0}
  html,body{width:1200px;height:592px;overflow:hidden}
  body{background:var(--canvas);font-family:"Open Sans",Arial,sans-serif;color:var(--ink);position:relative}

  .slide{position:absolute;width:342px;height:256px;background:var(--white);overflow:hidden;box-shadow:0 1px 3px rgba(0,0,0,.18)}
  .col-1{left:42px}.col-2{left:433px}.col-3{left:828px}
  .row-1{top:32px}.row-2{top:307px}

  .slide-header{position:absolute;left:0;top:0;width:100%;height:34px;
    background:linear-gradient(90deg,var(--plum) 0%,#a5246f 45%,var(--magenta) 100%);
    display:flex;align-items:center;padding:0 10px 0 12px}
  .slide-title{color:var(--white);font-weight:700;font-size:15px;flex:1;white-space:nowrap}
  .tagline{color:var(--white);font-weight:700;font-size:6.4px;margin-right:6px;white-space:nowrap}
  .brand{color:var(--white);font-weight:600;font-size:12px;white-space:nowrap}

  .slide-footer{position:absolute;left:0;bottom:0;width:100%;height:28px}
  .footer-rule{position:absolute;left:40px;right:0;top:7px;height:1px;background:var(--magenta-line)}
  .footer-url{position:absolute;right:38px;top:1px;font-size:7px;letter-spacing:.8px;color:var(--grey-text);background:var(--white);padding:0 4px}
  .copyright{position:absolute;left:38px;top:13px;font-size:6.8px;color:var(--grey-text)}
  .slide-number{position:absolute;left:16px;top:2px;width:15px;height:15px;background:var(--diamond);transform:rotate(45deg)}
  .slide-number span{display:block;transform:rotate(-45deg);color:var(--white);font-size:8px;font-weight:700;text-align:center;line-height:15px}

  .slide-cover{background:radial-gradient(ellipse at 50% 42%,#d8398f 0%,#b02a7d 40%,#7a1860 85%,#6a1455 100%)}
  .slide-cover .slide-footer .footer-url,.slide-cover .copyright{background:transparent;color:var(--white)}
  .slide-cover .footer-rule{background:#f05aa3}
  .slide-cover .slide-number{background:#c77ba9}
  .cover-block{position:absolute;left:0;right:0;top:80px;text-align:center;color:var(--white)}
  .cover-brand{font-size:22px;font-weight:600}
  .cover-tagline{font-size:7.5px;font-weight:700;margin-top:6px}
  .cover-name{font-size:14px;font-weight:700;margin-top:20px}
  .cover-date{font-size:13px;margin-top:2px}

  .bullets{position:absolute;left:20px;top:56px;list-style:none}
  .bullets li{position:relative;padding-left:10px;font-size:11.6px;line-height:15px;margin-bottom:21px;color:var(--ink)}
  .bullets li::before{content:"";position:absolute;left:0;top:5px;width:5px;height:5px;border-radius:50%;background:var(--bullet)}
  .bullets.tight li{margin-bottom:16px}
  .bullets.proposition{left:12px;top:53px}

  .mission{position:absolute;left:20px;right:20px;top:100px;text-align:center;font-size:11.8px;line-height:19.5px}

  .value-box{position:absolute;color:var(--white);padding:4px 7px}
  .value-box h3{font-size:11.5px;font-weight:700;margin-bottom:1px}
  .value-box ul{list-style:none}
  .value-box li{font-size:7.2px;line-height:12px}
  .value-box li::before{content:"• "}
  .value-energy{left:53px;top:61px;width:95px;height:73px;background:var(--energy)}
  .value-credibility{left:194px;top:61px;width:96px;height:73px;background:var(--credibility)}
  .value-relationships{left:111px;top:154px;width:119px;height:60px;background:var(--relationships)}

  .chart{position:absolute;left:22px;top:54px;width:310px;height:175px}
</style>
</head>
<body>

<section class="slide slide-cover col-1 row-1">
  <div class="cover-block">
    <div class="cover-brand">veraKorbell</div>
    <div class="cover-tagline">• Insight &nbsp;• Integrity &nbsp;• Impact.</div>
    <div class="cover-name">Martin Hale</div>
    <div class="cover-date">July 10, 2014</div>
  </div>
  <footer class="slide-footer">
    <div class="footer-rule"></div><div class="footer-url">www.verakorbell.co.uk</div>
    <div class="slide-number"><span>1</span></div>
    <div class="copyright">© veraKorbell Ltd. 2014 All Rights Reserved</div>
  </footer>
</section>

<section class="slide col-2 row-1">
  <header class="slide-header"><h2 class="slide-title">Martin Hale</h2><span class="tagline">• Insight &nbsp;• Integrity &nbsp;• Impact.</span><span class="brand">veraKorbell</span></header>
  <ul class="bullets tight">
    <li>Managing Director Kirowa UK</li>
    <li>CEO Meridian Health Co</li>
    <li>Managing Director Medical and Scientific</li>
    <li>Director Solvane Market<br>Access/HE/BD/NPP/BI/Training/GA/PA/KAM</li>
  </ul>
  <footer class="slide-footer">
    <div class="footer-rule"></div><div class="footer-url">www.verakorbell.co.uk</div>
    <div class="slide-number"><span>2</span></div>
    <div class="copyright">© veraKorbell Ltd. 2014 All Rights Reserved</div>
  </footer>
</section>

<section class="slide col-3 row-1">
  <header class="slide-header"><h2 class="slide-title">Mission</h2><span class="tagline">• Insight &nbsp;• Integrity &nbsp;• Impact.</span><span class="brand">veraKorbell</span></header>
  <p class="mission">Deliver Cutting Edge Performance With Our Clients Through The Best Relationships With Customers That Influence Access To Products And Services</p>
  <footer class="slide-footer">
    <div class="footer-rule"></div><div class="footer-url">www.verakorbell.co.uk</div>
    <div class="slide-number"><span>3</span></div>
    <div class="copyright">© veraKorbell Ltd. 2014 All Rights Reserved</div>
  </footer>
</section>

<section class="slide col-1 row-2">
  <header class="slide-header"><h2 class="slide-title">Values</h2><span class="tagline">• Insight &nbsp;• Integrity &nbsp;• Impact.</span><span class="brand">veraKorbell</span></header>
  <div class="value-box value-energy"><h3>Energy</h3><ul><li>Intensity</li><li>Fun</li><li>Determination</li><li>Fortitude</li></ul></div>
  <div class="value-box value-credibility"><h3>Credibility</h3><ul><li>Expertise</li><li>Experience</li><li>Professional</li><li>Constant learning</li></ul></div>
  <div class="value-box value-relationships"><h3>Relationships</h3><ul><li>Networking</li><li>Trust</li><li>Influencing at the top</li></ul></div>
  <footer class="slide-footer">
    <div class="footer-rule"></div><div class="footer-url">www.verakorbell.co.uk</div>
    <div class="slide-number"><span>4</span></div>
    <div class="copyright">© veraKorbell Ltd. 2014 All Rights Reserved</div>
  </footer>
</section>

<section class="slide col-2 row-2">
  <header class="slide-header"><h2 class="slide-title">Proposition</h2><span class="tagline">• Insight &nbsp;• Integrity &nbsp;• Impact.</span><span class="brand">veraKorbell</span></header>
  <ul class="bullets proposition">
    <li>Helios Director Team</li>
    <li>Helios Academy</li>
    <li>Value Proposition Build</li>
  </ul>
  <footer class="slide-footer">
    <div class="footer-rule"></div><div class="footer-url">www.verakorbell.co.uk</div>
    <div class="slide-number"><span>5</span></div>
    <div class="copyright">© veraKorbell Ltd. 2014 All Rights Reserved</div>
  </footer>
</section>

<section class="slide col-3 row-2">
  <header class="slide-header"><h2 class="slide-title"></h2><span class="tagline">• Insight &nbsp;• Integrity &nbsp;• Impact.</span><span class="brand">veraKorbell</span></header>
  <svg class="chart" viewBox="0 0 310 175" role="img" aria-label="Share of voice by product, January 2006 to January 2009">
    <defs>
      <linearGradient id="plotFill" x1="0" y1="0" x2="0" y2="1">
        <stop offset="0" stop-color="#fff"/>
        <stop offset="1" stop-color="#f7d3e6"/>
      </linearGradient>
    </defs>
    <rect x="0" y="0" width="300" height="10" fill="#bdbdbd"/>
    <text x="4" y="6.8" font-size="4.6" font-weight="700" fill="#fff">NOTE - In the C9C/D market, Velora never exceeded 5% share of voice</text>
    <rect x="22" y="20" width="226" height="125" fill="url(#plotFill)"/>
    <g stroke="#e7a6c8" stroke-width=".5">
      <line x1="22" x2="248" y1="145" y2="145"/><line x1="22" x2="248" y1="127.2" y2="127.2"/>
      <line x1="22" x2="248" y1="109.3" y2="109.3"/><line x1="22" x2="248" y1="91.4" y2="91.4"/>
      <line x1="22" x2="248" y1="73.6" y2="73.6"/><line x1="22" x2="248" y1="55.8" y2="55.8"/>
      <line x1="22" x2="248" y1="37.9" y2="37.9"/><line x1="22" x2="248" y1="20" y2="20"/>
    </g>
    <g font-size="4.4" fill="#333" text-anchor="end" font-weight="600">
      <text x="18" y="146.5">0.0%</text><text x="18" y="128.7">5.0%</text><text x="18" y="110.8">10.0%</text>
      <text x="18" y="92.9">15.0%</text><text x="18" y="75.1">20.0%</text><text x="18" y="57.3">25.0%</text>
      <text x="18" y="39.4">30.0%</text><text x="18" y="21.5">35.0%</text>
    </g>
    <g font-size="3.9" fill="#333" font-weight="600" text-anchor="end">
      <text transform="translate(23.5 149) rotate(-90)">Jan-06</text><text transform="translate(36.1 149) rotate(-90)">Mar-06</text>
      <text transform="translate(48.6 149) rotate(-90)">May-06</text><text transform="translate(61.2 149) rotate(-90)">Jul-06</text>
      <text transform="translate(73.7 149) rotate(-90)">Sept-06</text><text transform="translate(86.3 149) rotate(-90)">Nov-06</text>
      <text transform="translate(98.9 149) rotate(-90)">Jan-07</text><text transform="translate(111.4 149) rotate(-90)">Mar-07</text>
      <text transform="translate(124 149) rotate(-90)">May-07</text><text transform="translate(136.5 149) rotate(-90)">Jul-07</text>
      <text transform="translate(149.1 149) rotate(-90)">Sept-07</text><text transform="translate(161.7 149) rotate(-90)">Nov-07</text>
      <text transform="translate(174.2 149) rotate(-90)">Jan-08</text><text transform="translate(186.8 149) rotate(-90)">Mar-08</text>
      <text transform="translate(199.3 149) rotate(-90)">May-08</text><text transform="translate(211.9 149) rotate(-90)">Jul-08</text>
      <text transform="translate(224.5 149) rotate(-90)">Sept-08</text><text transform="translate(237 149) rotate(-90)">Nov-08</text>
      <text transform="translate(249.5 149) rotate(-90)">Jan-09</text>
    </g>
    <g fill="none" stroke-width="1.4" stroke-linejoin="round">
      <polyline stroke="#e6197a" points="22,141.4 34.6,137.9 47.1,137.9 59.7,137.9 72.2,139.6 84.8,139.6 97.4,141.4 109.9,141.4 122.5,145 135,143.2 147.6,141.4 160.2,141.4 172.7,141.4 185.3,137.9 197.8,132.5 210.4,130.7 223,128.9 235.5,134.3 248,123.6"/>
      <polyline stroke="#6a2c8e" points="22,70 34.6,59.3 47.1,52.2 59.7,48.6 72.2,55.8 84.8,66.5 97.4,91.4 109.9,91.4 122.5,77.2 135,66.5 147.6,91.4 160.2,91.4 172.7,73.6 185.3,48.6 197.8,66.5 210.4,77.2 223,98.6 235.5,102.2 248,105.7"/>
      <polyline stroke="#f7941d" points="22,84.3 34.6,87.9 47.1,80.7 59.7,87.9 72.2,91.4 84.8,84.3 97.4,84.3 109.9,98.6 122.5,77.2 135,62.9 147.6,66.5 160.2,66.5 172.7,80.7 185.3,73.6 197.8,73.6 210.4,70 223,62.9 235.5,45 248,41.5"/>
      <polyline stroke="#c4161c" points="22,34.3 34.6,41.5 47.1,45 59.7,41.5 72.2,37.9 84.8,73.6 97.4,84.3 109.9,95 122.5,102.2 135,116.4 147.6,127.2 160.2,120 172.7,95 185.3,112.9 197.8,127.2 210.4,130.7 223,130.7 235.5,134.3 248,134.3"/>
      <polyline stroke="#1fa39c" points="22,109.3 34.6,105.7 47.1,109.3 59.7,102.2 72.2,102.2 84.8,91.4 97.4,95 109.9,105.7 122.5,102.2 135,105.7 147.6,109.3 160.2,102.2 172.7,102.2 185.3,80.7 197.8,70 210.4,66.5 223,59.3 235.5,55.8 248,62.9"/>
      <polyline stroke="#8dc63f" points="22,102.2 34.6,102.2 47.1,98.6 59.7,95 72.2,98.6 84.8,87.9 97.4,84.3 109.9,95 122.5,84.3 135,77.2 147.6,66.5 160.2,77.2 172.7,87.9 185.3,84.3 197.8,95 210.4,98.6 223,102.2 235.5,91.4 248,80.7"/>
    </g>
    <g font-size="4.2" font-weight="700" fill="#333">
      <rect x="256" y="22" width="5" height="9" fill="#e6197a"/><text x="264" y="28">Velora</text>
      <rect x="256" y="36" width="5" height="9" fill="#6a2c8e"/><text x="264" y="39.5">Castrin +</text><text x="264" y="44.5">Castrincomp</text>
      <rect x="256" y="50" width="5" height="9" fill="#f7941d"/><text x="264" y="53.5">Arvelle +</text><text x="264" y="58.5">Coarvelle</text>
      <rect x="256" y="64" width="5" height="9" fill="#c4161c"/><text x="264" y="67.5">Dintra +</text><text x="264" y="72.5">Codintra</text>
      <rect x="256" y="78" width="5" height="9" fill="#1fa39c"/><text x="264" y="81.5">Meltrix +</text><text x="264" y="86.5">Meltrixplus</text>
      <rect x="256" y="92" width="5" height="9" fill="#8dc63f"/><text x="264" y="95.5">Olvessa +</text><text x="264" y="100.5">Olvessaplus</text>
    </g>
  </svg>
  <footer class="slide-footer">
    <div class="footer-rule"></div><div class="footer-url">www.verakorbell.co.uk</div>
    <div class="slide-number"><span>6</span></div>
    <div class="copyright">© veraKorbell Ltd. 2014 All Rights Reserved</div>
  </footer>
</section>

</body>
</html>
```